Sunscreen Package Design Modern SPF 50

Update current package design to a more modern design target women 16-40 Do not make it playful. Solvane is home to movie stars and high income business people PalmSprings is one of the most desired vacation areas in the world. The sun shines 350 days a year. World class Tennis and Golf tournaments are held every year with the worlds top players attending these tournaments

Target Market(s)

Women

Industry/Entity Type

Skin Protection

Font styles to use
Sans Serif

Requirements
Must have
• The words Solvane and VELORIMA

```html
<!DOCTYPE html>
<html lang="en">
<head>
<meta charset="utf-8">
<title>Solvane VELORIMA — Aftersun &amp; Sunscreen Tubes</title>
<link href="https://fonts.googleapis.com/css2?family=Montserrat:wght@500&amp;family=Libre+Baskerville:ital,wght@0,400;0,700;1,400&amp;display=swap" rel="stylesheet">
<style>
  :root {
    --canvas: #ffffff;
    --aqua: #94b9be;
    --aqua-deep: #6d9aa1;
    --clay: #d49370;
    --clay-deep: #b8724b;
    --tube-white: #f1f0ec;
    --cap-white: #ebeae6;
    --name-stone: #e2deda;
    --ink: #3b3b3b;
  }
  html, body {
    margin: 0;
    padding: 0;
    width: 1200px;
    height: 956px;
    overflow: hidden;
    background: var(--canvas);
  }
  .product-line {
    display: block;
    width: 1200px;
    height: 956px;
  }
  .brand-name {
    font-family: "Montserrat", sans-serif;
    font-weight: 500;
    font-size: 11px;
    letter-spacing: 2.6px;
    fill: var(--name-stone);
    text-anchor: start;
  }
  .product-title {
    font-family: "Libre Baskerville", serif;
    fill: var(--tube-white);
    text-anchor: middle;
    letter-spacing: 5px;
    font-size: 14px;
  }
  .fine-print {
    font-family: "Libre Baskerville", serif;
    text-anchor: middle;
    font-size: 2.6px;
    fill: var(--ink);
  }
  .fine-print--light { fill: #ffffff; letter-spacing: 0.2px; }
  .spf-label {
    font-family: "Libre Baskerville", serif;
    font-size: 11px;
    fill: var(--clay-deep);
    text-anchor: middle;
  }
  .volume { font-family: "Libre Baskerville", serif; font-size: 4.5px; text-anchor: middle; }
  .volume--aqua { fill: var(--aqua-deep); }
  .volume--clay { fill: var(--clay-deep); }
</style>
</head>
<body>
<svg class="product-line" viewBox="0 0 1200 956" xmlns="http://www.w3.org/2000/svg">
  <defs>
    <linearGradient id="aquaBody" x1="0" x2="1" y1="0" y2="0">
      <stop offset="0" stop-color="#a9cfd4"/>
      <stop offset="1" stop-color="#4f7d83"/>
    </linearGradient>
    <linearGradient id="clayBody" x1="0" x2="1" y1="0" y2="0">
      <stop offset="0" stop-color="#eaae86"/>
      <stop offset="1" stop-color="#8c5128"/>
    </linearGradient>
  </defs>

  <!-- Aftersun tube -->
  <g class="tube tube--aftersun">
    <rect class="tube-seal" x="277" y="191" width="277" height="29" fill="var(--aqua)"/>
    <path class="tube-body" d="M278 220 L553 220 L501 570 L332 570 Z" fill="url(#aquaBody)"/>
    <path class="tube-base" d="M332 570 L501 570 L493 652 Q492 660 484 660 L349 660 Q341 660 340 652 Z" fill="var(--tube-white)"/>
    <rect class="tube-cap" x="340" y="660" width="153" height="102" rx="3" fill="var(--cap-white)"/>

    <g class="brand-lockup">
      <circle cx="347" cy="366" r="5" fill="var(--name-stone)"/>
      <text class="brand-name" x="358" y="370">SOLVANE VELORIMA</text>
    </g>

    <text class="product-title" x="416" y="564">AFTERSUN</text>
    <text class="fine-print" x="416" y="580">HYDRATE YOUR SKIN WITH THESE ESSENTIAL INGREDIENTS</text>
    <text class="fine-print" x="416" y="584">- Hyaluronic Acid <tspan font-style="italic" font-weight="700">Cucumber Aloe Jojoba Sunflower</tspan> -</text>
    <text class="volume volume--aqua" x="416" y="641">3 fl oz / 88 ml</text>
  </g>

  <!-- Sunscreen tube -->
  <g class="tube tube--sunscreen">
    <rect class="tube-seal" x="640" y="191" width="277" height="29" fill="var(--clay)"/>
    <path class="tube-body" d="M641 220 L916 220 L864 570 L695 570 Z" fill="url(#clayBody)"/>
    <path class="tube-base" d="M695 570 L864 570 L856 652 Q855 660 847 660 L712 660 Q704 660 703 652 Z" fill="var(--tube-white)"/>
    <rect class="tube-cap" x="703" y="660" width="153" height="102" rx="3" fill="var(--cap-white)"/>

    <g class="brand-lockup">
      <circle cx="710" cy="366" r="5" fill="var(--name-stone)"/>
      <text class="brand-name" x="721" y="370">SOLVANE VELORIMA</text>
    </g>

    <text class="product-title" x="779" y="559">SUNSCREEN</text>
    <text class="fine-print fine-print--light" x="779" y="565">UVA + UVB PROTECTION &#160;|&#160; BROAD SPECTRUM</text>
    <text class="spf-label" x="779" y="584">SPF <tspan font-weight="700">30</tspan></text>
    <text class="fine-print" x="779" y="589">Water Resistant (80 Minutes)</text>
    <text class="volume volume--clay" x="779" y="641">3 fl oz / 88 ml</text>
  </g>
</svg>
</body>
</html>
```